Our company TrulaPay, an online processor of payments is seeking talented submissions for our website redesign. The winning design will be chopped up and converted into a WordPress theme to allow for easy content additions and updates.

We are looking for modern designs that rival current websites in our industry (plimo.example, zanquetto.example, holvix.example, brandle.example, quillmarkcharges.example, evensplitcharges.example, KoboRun.example).

Our company is seeking to expand our reach to software developers and engineers who are either integrating our payment platform into their offerings or are engineering a custom solution for the company they work for and are in need of a payment platform such as our own.

We currently work with hundreds of different business partners whom either resell our services or integrate our processing capabilities into their software (which they sell). We also must communicate effectively to end users, businesses, who seek us out directly for their payment processing needs.

We are open to different color schemes but would ultimately like them to be somewhat inline with our current logo (see attached). Our website needs to instill security and confidence to any current and/or potential user as we are trusted with private and sensitive information.

We are seeking submissions from qualified; individual freelancers, freelance teams, and agencies who can attack this project in its entirety. Since this project is a total redesign, we would like submissions that have the capability to design any custom graphics, icons, buttons, and illustrations in line with our industry, capabilities, offerings, and content. We are looking for someone to design our new website and would prefer a vendor who can also help us to design elements (graphics, illustrations, charts, workflows) within our website.

Designs will be converted into a wordpress theme and we would like to utilize widgets for as many areas as possible to make editing and updating easy.

We are seeking the creation of a few unique pages but many of the pages for the majority of our content will just be internal content pages which will be duplicated.

We will likely contract with the winning submission for future work.

Please see Design Reference Document for more information

Target Market(s)

Resellers
Merchant Service Providers
Software Developers
Independent Sales Organizations (ISOs)
App Builders
Mobile App Builders
Independent Software Developers
Organizational Software Developers
Businesses who need to accept payments
Governments
Municipalities
Schools
DMVs
Courts
Retailers
Medical Offices
Hosipitals
Clinics
Dr. Offices
Gyms
Churches
Non-Profits
Software Companies
Technology Companies
Startups

• Logo cannot change drastically.

```html
<!DOCTYPE html>
<html lang="en">
<head>
<meta charset="utf-8">
<title>TrulaPay – Payment Processing</title>
<link rel="stylesheet" href="https://fonts.googleapis.com/css2?family=Ubuntu:ital,wght@0,400;0,500;0,700;1,400&family=Arimo:ital,wght@0,400;0,700;1,700&display=swap">
<style>
:root{
  --bar:#1a1a1a;
  --bar-top:#3a3a3a;
  --sky:#b9d3e6;
  --steel:#e9e9e9;
  --navy:#0a0a8c;
  --brand-red:#e30c0c;
  --ink:#222;
  --text:#444;
  --muted:#8a8a8a;
  --link-blue:#1a6cc4;
  --white:#fff;
  --rule:#d2d2d2;
  --foot-head:#f2f2f2;
}
*{box-sizing:border-box;margin:0;padding:0}
html,body{width:818px;height:1200px;overflow:hidden;background:#fff}
body{position:relative;font-family:"Arimo",Arial,sans-serif;color:var(--text)}
.abs{position:absolute}
.page{left:11px;top:9px;width:796px;height:1184px;
  background:linear-gradient(180deg,var(--sky) 0,#cfdfea 260px,var(--steel) 460px,#e6e6e6 100%)}
.topbar{left:11px;top:9px;width:796px;height:36px;background:linear-gradient(180deg,var(--bar-top),var(--bar));
  box-shadow:0 2px 3px rgba(0,0,0,.4)}
.call-top{right:200px;top:8px;font-family:"Ubuntu",sans-serif;font-size:15px;color:#9a9a9a;white-space:nowrap}
.call-top b{color:#fff;font-weight:400}
.pill-btn{top:9px;height:15px;background:linear-gradient(#2a78d8,#0a4ab0);color:#fff;border-radius:2px;
  font-size:8px;font-weight:700;display:flex;align-items:center;gap:4px;padding:0 8px;font-family:"Arimo",sans-serif}
.logo{left:72px;top:60px;display:flex;align-items:center;gap:8px}
.logo-mark{width:14px;height:14px;background:var(--brand-red);border-radius:50%}
.logo-name{font-family:"Ubuntu",sans-serif;font-size:30px;font-weight:500;color:var(--navy);line-height:1}
.logo-tag{left:94px;top:94px;font-size:9px;font-weight:700;color:#111;line-height:11px}
.nav{left:72px;top:129px;display:flex;align-items:center;font-family:"Ubuntu",sans-serif;font-size:13px;color:#222}
.nav a{padding:0 10px;height:28px;line-height:28px;border-right:1px solid #c6d6e2}
.nav a:last-child{border:none}
.nav .current{background:var(--navy);color:#fff;padding:0 6px;margin-right:4px;border:none}
.search{left:602px;top:138px;width:148px;height:18px;background:#fff;border-radius:9px;border:1px solid #cfd8de;
  font-size:8px;font-style:italic;color:#777;padding:4px 12px}
.search svg{position:absolute;right:7px;top:4px}
.hero{left:72px;top:164px;width:678px;height:274px;background:#fff;box-shadow:0 1px 4px rgba(0,0,0,.3)}
.hero-photo{left:78px;top:169px;width:666px;height:153px;
  background:linear-gradient(100deg,#c9a080 0%,#8e8e96 35%,#5f7fb8 60%,#b7bcc5 85%,#e0e2e6 100%)}
.panel{top:322px;height:110px;padding:7px 10px;color:#fff;font-size:8.6px;line-height:12.8px}
.panel-blue{left:78px;width:332px;background:var(--navy)}
.panel-red{left:410px;width:334px;background:var(--brand-red)}
.panel .more{position:absolute;bottom:6px;left:10px;font-style:italic;font-size:8px}
.tab{top:306px;width:32px;height:18px;border-radius:16px 16px 0 0}
.tagline{left:72px;top:473px;width:678px;height:58px;border-top:1px solid var(--rule);border-bottom:1px solid var(--rule);
  text-align:center;font-family:"Ubuntu",sans-serif;font-style:italic;color:#333}
.tagline .t1{font-size:17px;margin-top:7px}
.tagline .t2{font-size:12px;margin-top:5px}
.sec-title{font-family:"Ubuntu",sans-serif;font-weight:700;font-size:17px;color:var(--ink)}
.card-title{font-family:"Ubuntu",sans-serif;font-weight:700;font-size:11.5px;color:var(--ink)}
.body-copy{font-size:9px;line-height:14px;color:var(--text)}
.btn-dark{height:15px;background:linear-gradient(#4a4a4a,#151515);color:#fff;font-size:8px;font-weight:700;font-style:italic;
  padding:0 5px;line-height:15px;box-shadow:1px 1px 2px rgba(0,0,0,.4)}
.industry{left:534px;top:586px;list-style:none;font-size:9.5px;color:#333}
.industry li{display:flex;align-items:center;gap:10px;height:21.5px}
.industry li::before{content:"";width:13px;height:13px;background:linear-gradient(#9a9a9a,#6e6e6e);border:1px solid #ddd}
.rule{left:72px;width:678px;height:1px;background:var(--rule)}
.thumb{width:216px;height:108px;background:#fff;box-shadow:0 1px 3px rgba(0,0,0,.3);padding:6px}
.thumb-inner{width:100%;height:100%}
.cards{display:grid;grid-template-columns:repeat(4,1fr);gap:5px 7px;padding:2px 6px}
.cards span{height:26px;border-radius:3px;border:1px solid #ccc}
.footer{left:11px;top:1040px;width:796px;height:153px;background:#1b1b1b}
.foot-head{font-family:"Ubuntu",sans-serif;font-weight:500;font-size:12px;color:var(--foot-head);letter-spacing:.3px}
.foot-list{font-size:10px;color:#6d6d6d;line-height:17.5px;list-style:none}
.foot-call{left:537px;top:1084px;font-family:"Ubuntu",sans-serif;font-size:17px;color:#7a7a7a}
.foot-call b{color:var(--link-blue);font-weight:400}
.social{display:flex;gap:14px}
.social span{width:22px;height:22px;background:#666;border-radius:3px}
.social span:first-child{border-radius:50%}
.foot-rule{left:74px;top:1158px;width:676px;height:1px;background:#333}
.copyright{left:74px;top:1168px;font-size:8.6px;color:#fff}
.legal{left:606px;top:1170px;font-size:8.6px;color:#fff}
</style>
</head>
<body>
<div class="abs page"></div>
<div class="abs topbar"></div>
<div class="abs call-top">Call Us Now: <b>555 014 2290</b></div>
<div class="abs pill-btn" style="left:628px">
  <svg width="8" height="6"><rect width="8" height="6" fill="#fff"/><path d="M0 0 4 3 8 0" stroke="#0a4ab0" fill="none"/></svg>Email Us</div>
<div class="abs pill-btn" style="left:693px;width:58px">
  <svg width="6" height="7"><rect y="3" width="6" height="4" fill="#fff"/><path d="M1 3V2a2 2 0 0 1 4 0v1" stroke="#fff" fill="none"/></svg>Login</div>

<div class="abs logo"><span class="logo-name">TrulaPay</span><span class="logo-mark"></span></div>
<div class="abs logo-tag">Electronic ACH<br>&nbsp;&nbsp;&nbsp;Processing</div>

<nav class="abs nav">
  <a class="current">Home</a><a>Solutions</a><a>Developers</a><a>Partners</a><a>Company</a><a>Resources</a><a>Blog</a>
</nav>
<div class="abs search">Search line
  <svg width="10" height="10"><circle cx="4" cy="4" r="3" stroke="#888" fill="none" stroke-width="1.4"/><path d="M6 6 9 9" stroke="#888" stroke-width="1.6"/></svg>
</div>

<div class="abs hero"></div>
<div class="abs hero-photo" role="img" aria-label="Photo of a hand holding a payment card above a laptop keyboard"></div>
<div class="abs tab" style="left:78px;background:var(--navy)"></div>
<div class="abs tab" style="left:410px;background:var(--brand-red)"></div>
<div class="abs panel panel-blue">Merchants, Businesses, I have a business, Online Payment Processing, SaaS<br>This interactive graphic box will convey to the website visitor that this is where you click if you are a business and need to get setup to accept payments for your business with us.<br>Something along the lines of maybe some skyscrapers, maybe a business disctrict<span class="more">click here...</span></div>
<div class="abs panel panel-red">Developers, I Develop Software, Software Application Developers, Payment Processing API<br>Software Developers, Start-ups. Users who are looking to integrate a payment platform into their; website, ERP, CMS, mobile solution, software offering, some type of advanced integration requiring a custom integration with a payment processing platform, PaaS.<span class="more">click here...</span></div>

<div class="abs tagline">
  <p class="t1">Payment Processing for the 21st Century.</p>
  <p class="t2">TrulaPay provides the software, technology, and platform for multi-channel payment acceptance</p>
</div>

<h2 class="abs sec-title" style="left:72px;top:551px">About Us</h2>
<p class="abs body-copy" style="left:72px;top:580px;width:440px">Since 1992 we have been helping merchants streamline their payment acceptance. Whether your acceptance needs are online, at the poin-of-sale, or mobile; TrulaPay can help.<br><br>We provide both “out-of -the-box ” and custom solutions for your company or organization to begin taking paymentsin line with your needs and desires.</p>
<div class="abs btn-dark" style="left:72px;top:675px">Continue reading →</div>

<h2 class="abs sec-title" style="left:534px;top:551px">Custom Industry Solutions</h2>
<ul class="abs industry">
  <li>Custom Industry Solutions</li><li>Government</li><li>Medical</li><li>Fitness</li><li>Martial Arts</li><li>Alarm Monitoring</li><li>Property Management</li>
</ul>

<div class="abs rule" style="top:740px"></div>
<h2 class="abs sec-title" style="left:72px;top:754px">ACH Payment Processing</h2>

<h3 class="abs card-title" style="left:72px;top:788px">Payment Gateway</h3>
<div class="abs thumb" style="left:72px;top:812px">
  <div class="thumb-inner cards" role="img" aria-label="Grid of accepted payment method badges">
    <span style="background:#f3e3b0"></span><span style="background:#f2c94c"></span><span style="background:#3b6fb0"></span><span style="background:#222"></span>
    <span style="background:#f2f2f2"></span><span style="background:#f6f0e6"></span><span style="background:#e4ecf8"></span><span style="background:#555"></span>
    <span style="background:#c0392b"></span><span style="background:#1d4e9a"></span><span style="background:#7a2a8c"></span><span style="background:#eee"></span>
  </div>
</div>
<p class="abs body-copy" style="left:72px;top:932px;width:216px">Lorem ipsum dolor sit amet, consectetu fringilla. Aenean quis nunc ipsum. Aliquam in ultrices diam. Nulla eu lacus vel</p>
<div class="abs btn-dark" style="left:72px;top:985px">View details →</div>

<h3 class="abs card-title" style="left:303px;top:788px">ACH Payment API</h3>
<div class="abs thumb" style="left:303px;top:812px">
  <div class="thumb-inner" style="border:1px solid #ddd;display:flex;flex-direction:column;align-items:center;justify-content:center;gap:4px">
    <div style="display:flex;align-items:center;gap:8px"><span class="logo-name" style="font-size:32px">TrulaPay</span><span class="logo-mark"></span></div>
    <span style="font-size:10px;font-weight:700;color:#111">Electronic Payment Processing</span>
  </div>
</div>
<p class="abs body-copy" style="left:303px;top:932px;width:216px">Lorem ipsum dolor sit amet, consectetu fringilla. Aenean quis nunc ipsum. Aliquam in ultrices diam. Nulla eu lacus vel</p>
<div class="abs btn-dark" style="left:303px;top:985px">View details →</div>

<h3 class="abs card-title" style="left:534px;top:788px">Processing for Software Development</h3>
<div class="abs thumb" style="left:534px;top:812px">
  <div class="thumb-inner" role="img" aria-label="Blue close-up of binary digits on a screen" style="background:linear-gradient(160deg,#0c5a78,#1e9fc4 55%,#0a3e5a)"></div>
</div>
<p class="abs body-copy" style="left:534px;top:932px;width:216px">Lorem ipsum dolor sit amet, consectetu fringilla. Aenean quis nunc ipsum. Aliquam in ultrices diam. Nulla eu lacus vel</p>
<div class="abs btn-dark" style="left:534px;top:985px">View details →</div>

<div class="abs rule" style="top:1020px"></div>

<footer class="abs footer"></footer>
<h4 class="abs foot-head" style="left:74px;top:1056px">GET IN TOUCH!</h4>
<ul class="abs foot-list" style="left:74px;top:1075px"><li>Address:</li><li>City:</li><li>Country:</li><li>Email:</li></ul>
<ul class="abs foot-list" style="left:123px;top:1075px"><li>Lorem ipsum dolor</li><li>Aonsect adipisic</li><li>Eiusmjkod tempor</li><li>Incididunt ut labore</li></ul>
<h4 class="abs foot-head" style="left:249px;top:1056px">WHY US</h4>
<ul class="abs foot-list" style="left:250px;top:1075px"><li>• Lorem ipsum dolor</li><li>• Aonsect adipisic</li><li>• Eiusmjkod tempor</li><li>• Incididunt ut labore</li></ul>
<h4 class="abs foot-head" style="left:379px;top:1056px">FOLLOW US ON</h4>
<div class="abs social" style="left:374px;top:1085px"><span></span><span></span><span></span></div>
<div class="abs foot-call">Call Us Now: <b>555 014 2290</b></div>
<div class="abs foot-rule"></div>
<p class="abs copyright">© Copyright 2010 TrulaPay. All Rights Reserved.</p>
<p class="abs legal">Privacy Policy &nbsp;|&nbsp; Terms &amp; Conditions</p>
</body>
</html>
```